Managed Services Provider for Medical Practices Business Card Design

We need a business card design for a new company based in the Illawarra region on NSW Australia, with intentions of expanding further into other regions. We provide I.T. managed services, server, printer, phone and hardware procurement and installations. We specialise in Medical Practices e.g. General Practitioners, Surgeons and other medical specialists etc. We would like to see colours that theme with our website. The final design should communicate integrity, strength, security and reliability.

Security

Velbrook Omnilux, Dorian Pakula, Shop 42 Cardwell Arcade, 517 Fenwick Orchard Road Marlowe Bay QLD 4821, Partner - Senior Technician, Ph: 0488 371 590, Email: dorian@omnilux.net.au, Web: www.omnilux.net.au

Velbrook Omnilux, Evan Brockwirth, Shop 42 Cardwell Arcade, 517 Fenwick Orchard Road Marlowe Bay QLD 4821, Partner - Senior Technician, Ph: 0461 937 025, Email: evan@omnilux.net.au, Web: www.omnilux.net.au

```html
<!DOCTYPE html>
<html lang="en">
<head>
<meta charset="utf-8">
<title>Velbrook Omnilux – Business Card Concepts</title>
<link rel="stylesheet" href="https://fonts.googleapis.com/css2?family=Arimo:wght@400;700&family=Questrial&display=swap">
<style>
  :root {
    --green: #62b92a;
    --green-bright: #6cc41f;
    --green-deep: #1f4d06;
    --green-mid: #2f7410;
    --charcoal: #2b2b2b;
    --charcoal-light: #3c3c3c;
    --silver-1: #cfcfcf;
    --silver-2: #f7f7f7;
    --text-dark: #333333;
    --white: #ffffff;
  }
  * { margin: 0; padding: 0; box-sizing: border-box; }
  html, body { width: 1200px; height: 823px; overflow: hidden; background: var(--white); }
  body { position: relative; font-family: "Questrial", sans-serif; color: var(--text-dark); }

  .option-label { position: absolute; font-family: "Arimo", sans-serif; font-size: 24px; color: #222; }

  .card { position: absolute; width: 522px; height: 315px; overflow: hidden; }
  .card--silver {
    background: linear-gradient(115deg, var(--silver-1) 0%, var(--silver-2) 30%, #d8d8d8 55%, var(--silver-2) 80%, #dcdcdc 100%);
    border: 1px solid #e2e2e2;
  }
  .card--green { background: linear-gradient(180deg, var(--green-mid) 0%, var(--green-deep) 100%); }

  .top-rule { position: absolute; left: 0; top: 0; width: 100%; height: 8px; background: var(--green); }

  .footer-band { position: absolute; left: 0; bottom: 0; width: 100%; height: 36px; }
  .footer-band svg { position: absolute; inset: 0; }
  .footer-url {
    position: absolute; left: 42px; bottom: 9px;
    font-family: "Arimo", sans-serif; font-weight: 700; font-size: 15px; color: var(--charcoal);
  }

  .brand { position: absolute; display: flex; align-items: center; gap: 10px; }
  .brand-mark { width: 14px; height: 14px; background: var(--green); flex: none; }
  .brand-name { font-family: "Arimo", sans-serif; font-weight: 700; color: var(--green); white-space: nowrap; letter-spacing: 0.5px; line-height: 1; }
  .brand-division { position: absolute; font-family: "Arimo", sans-serif; font-size: 8px; line-height: 1; color: var(--charcoal); white-space: nowrap; }

  .dark-band {
    position: absolute; left: 0; width: 100%;
    background: linear-gradient(180deg, #1a1a1a 0%, var(--charcoal-light) 50%, #1e1e1e 100%);
  }
  .green-head { position: absolute; left: 0; top: 0; width: 100%; background: linear-gradient(180deg, var(--green-bright) 0%, #4d9a14 100%); }

  .person-name { position: absolute; font-family: "Arimo", sans-serif; font-weight: 700; font-size: 16px; line-height: 1.2; }
  .person-role { position: absolute; font-size: 14.5px; line-height: 1.2; }
  .contact-line { position: absolute; display: flex; align-items: center; gap: 7px; font-size: 14.5px; line-height: 1.2; white-space: nowrap; }
  .contact-line svg { width: 13px; height: 13px; flex: none; }
  .company { position: absolute; text-align: right; white-space: nowrap; }
  .company-name { font-family: "Arimo", sans-serif; font-weight: 700; font-size: 16px; line-height: 1.2; }
  .company-address { font-size: 14px; line-height: 23px; margin-top: 18px; }

  .card--green .person-name, .card--green .person-role, .card--green .contact-line,
  .card--green .company { color: var(--white); }
  .web-center { position: absolute; width: 100%; text-align: center; font-family: "Arimo", sans-serif; font-weight: 700; font-size: 14px; color: var(--white); }
</style>
</head>
<body>

<div class="option-label" style="left:297px; top:26px;">1</div>
<div class="option-label" style="left:882px; top:17px;">2</div>

<!-- Option 1 front -->
<section class="card card--silver" style="left:45px; top:58px;">
  <div class="top-rule"></div>
  <div class="brand" style="left:48px; top:124px;">
    <span class="brand-mark"></span>
    <span class="brand-name" style="font-size:36px;">Velbrook Omnilux</span>
  </div>
  <div class="brand-division" style="left:48px; top:166px;">A Division of Velbrook Computers Pty Ltd ©</div>
  <div class="footer-band">
    <svg viewBox="0 0 522 36" preserveAspectRatio="none">
      <rect width="522" height="36" fill="var(--green)"/>
      <polygon points="232,0 522,0 522,20 268,20" fill="var(--white)"/>
      <polygon points="250,0 522,0 522,14 276,14" fill="var(--charcoal)"/>
    </svg>
    <span class="footer-url">www.omnilux.net.au</span>
  </div>
</section>

<!-- Option 1 back -->
<section class="card card--silver" style="left:45px; top:435px;">
  <div class="top-rule"></div>
  <div class="brand" style="left:212px; top:54px;">
    <span class="brand-mark" style="width:10px;height:10px;"></span>
    <span class="brand-name" style="font-size:22px;">Velbrook Omnilux</span>
  </div>
  <div class="person-name" style="left:42px; top:121px;">Evan Brockwirth</div>
  <div class="person-role" style="left:42px; top:147px;">Partner - Senior Technician</div>
  <div class="contact-line" style="left:42px; top:186px;">
    <svg viewBox="0 0 16 16"><path d="M4 1l3 3-2 2c1 2 3 4 5 5l2-2 3 3-2 3C7 15 1 9 1 3z" fill="none" stroke="currentColor" stroke-width="1.4"/></svg>
    0461 937 025
  </div>
  <div class="contact-line" style="left:42px; top:209px;">
    <svg viewBox="0 0 16 16"><rect x="1" y="3" width="14" height="10" fill="none" stroke="currentColor" stroke-width="1.3"/><path d="M1 3l7 6 7-6" fill="none" stroke="currentColor" stroke-width="1.3"/></svg>
    evan@omnilux.net.au
  </div>
  <div class="company" style="right:45px; top:121px;">
    <div class="company-name">Velbrook Omnilux</div>
    <div class="company-address">Shop 42 Cardwell Arcade,<br>517 Fenwick Orchard Road<br>Marlowe Bay QLD 4821</div>
  </div>
  <div class="footer-band">
    <svg viewBox="0 0 522 36" preserveAspectRatio="none">
      <rect width="522" height="36" fill="var(--green)"/>
      <polygon points="232,0 522,0 522,20 268,20" fill="var(--white)"/>
      <polygon points="250,0 522,0 522,14 276,14" fill="var(--charcoal)"/>
    </svg>
    <span class="footer-url">www.omnilux.net.au</span>
  </div>
</section>

<!-- Option 2 front -->
<section class="card card--green" style="left:634px; top:58px; height:316px;">
  <div class="green-head" style="height:97px;"></div>
  <div class="dark-band" style="top:97px; height:100px;"></div>
  <div class="brand" style="left:50px; top:132px;">
    <span class="brand-mark"></span>
    <span class="brand-name" style="font-size:34px;">Velbrook Omnilux</span>
  </div>
  <div class="brand-division" style="left:50px; top:172px; color:var(--white);">A Division of Velbrook Computers Pty Ltd ©</div>
  <div class="web-center" style="top:216px;">www.omnilux.net.au</div>
</section>

<!-- Option 2 back -->
<section class="card card--green" style="left:632px; top:432px;">
  <div class="green-head" style="height:16px;"></div>
  <div class="dark-band" style="top:16px; height:100px;"></div>
  <div class="brand" style="left:50px; top:50px;">
    <span class="brand-mark"></span>
    <span class="brand-name" style="font-size:34px;">Velbrook Omnilux</span>
  </div>
  <div class="person-name" style="left:50px; top:145px;">Dorian Pakula</div>
  <div class="person-role" style="left:50px; top:167px;">Partner - Senior Technician</div>
  <div class="contact-line" style="left:50px; top:204px; font-size:16px;">
    <svg viewBox="0 0 16 16"><path d="M4 1l3 3-2 2c1 2 3 4 5 5l2-2 3 3-2 3C7 15 1 9 1 3z" fill="none" stroke="currentColor" stroke-width="1.4"/></svg>
    0488 371 590
  </div>
  <div class="contact-line" style="left:50px; top:231px;">
    <svg viewBox="0 0 16 16"><rect x="1" y="3" width="14" height="10" fill="none" stroke="currentColor" stroke-width="1.3"/><path d="M1 3l7 6 7-6" fill="none" stroke="currentColor" stroke-width="1.3"/></svg>
    dorian@omnilux.net.au
  </div>
  <div class="contact-line" style="left:50px; top:258px;">
    <svg viewBox="0 0 16 16"><circle cx="8" cy="8" r="6.5" fill="none" stroke="currentColor" stroke-width="1.2"/><ellipse cx="8" cy="8" rx="3" ry="6.5" fill="none" stroke="currentColor" stroke-width="1.1"/><path d="M1.5 8h13M2.5 5h11M2.5 11h11" stroke="currentColor" stroke-width="1"/></svg>
    www.omnilux.net.au
  </div>
  <div class="company" style="right:48px; top:145px;">
    <div class="company-name">Velbrook Omnilux</div>
    <div class="company-address">Shop 42 Cardwell Arcade,<br>517 Fenwick Orchard Road<br>Marlowe Bay QLD 4821</div>
  </div>
</section>

</body>
</html>
```